Hair & Skin Product Line

I need someone to design clear product labels that can go on pink bottles. I'm looking for someone who can add graphics such as avocado and honey to the label as these are ingredients in our products. The colors we want incorporated are gold, blue, white and purple. I will upload information about our company identity and information on one label. Whoever we choose, we will use them to create 11 more labels.

Target Market(s)

Woman 25-50, Natural, straight or curly hair.

Industry/Entity Type

Beauty

```html
<!DOCTYPE html>
<html lang="en">
<head>
<meta charset="utf-8">
<title>Avocado &amp; Honey Shampoo Label</title>
<link href="https://fonts.googleapis.com/css2?family=Montserrat:wght@400;500;600;700&family=Dancing+Script:wght@500&display=swap" rel="stylesheet">
<style>
  :root {
    --page-bg: #ffffff;
    --label-pink: #eeb0c9;
    --band-blue: #4b5b9c;
    --ink-dark: #3b3a3c;
    --script-blue: #6674c0;
    --gold-dark: #8a6a3c;
    --gold-mid: #c9a46a;
    --gold-light: #e8cf9c;
    --soft-white: #ffffff;
    --art-green: #8fae5a;
    --art-honey: #e9a72a;
  }
  html, body {
    margin: 0;
    padding: 0;
    width: 1200px;
    height: 1200px;
    overflow: hidden;
    background: var(--page-bg);
  }
  .canvas {
    position: relative;
    width: 1200px;
    height: 1200px;
  }
  .label {
    position: absolute;
    left: 390px;
    top: 65px;
    width: 420px;
    height: 1070px;
    background: var(--label-pink);
    font-family: "Montserrat", sans-serif;
    color: var(--ink-dark);
  }
  .brand-band {
    position: absolute;
    left: 132px;
    top: 0;
    width: 154px;
    height: 333px;
    background: var(--band-blue);
  }
  .brand-name {
    position: absolute;
    left: 50%;
    top: 150px;
    transform: translate(-50%, -50%) rotate(-90deg);
    white-space: nowrap;
    font-family: "Montserrat", sans-serif;
    font-weight: 500;
    font-size: 26px;
    letter-spacing: 1px;
    color: var(--soft-white);
  }
  .ingredient-art {
    position: absolute;
    left: 18px;
    top: 350px;
    width: 384px;
    height: 236px;
    border-radius: 24px;
    background: radial-gradient(ellipse at 30% 45%, rgba(143,174,90,0.75), rgba(143,174,90,0) 60%),
                radial-gradient(ellipse at 50% 70%, rgba(233,167,42,0.7), rgba(233,167,42,0) 55%),
                radial-gradient(ellipse at 75% 40%, rgba(120,150,80,0.7), rgba(120,150,80,0) 60%);
  }
  .product-title {
    position: absolute;
    left: 0;
    width: 100%;
    top: 600px;
    margin: 0;
    text-align: center;
    font-weight: 700;
    font-size: 36px;
    line-height: 38px;
    letter-spacing: 0.5px;
    color: var(--ink-dark);
  }
  .product-type {
    position: absolute;
    left: 0;
    width: 100%;
    top: 662px;
    text-align: center;
    font-family: "Dancing Script", cursive;
    font-weight: 500;
    font-size: 56px;
    line-height: 60px;
    color: var(--script-blue);
  }
  .product-benefit {
    position: absolute;
    left: 0;
    width: 100%;
    top: 728px;
    text-align: center;
    font-weight: 600;
    font-size: 18px;
    letter-spacing: 0.5px;
    color: var(--ink-dark);
  }
  .infusion-ribbon {
    position: absolute;
    left: 66px;
    top: 760px;
    width: 288px;
    height: 32px;
    line-height: 32px;
    text-align: center;
    background: linear-gradient(90deg, var(--gold-dark), var(--gold-light) 45%, var(--gold-mid) 70%, var(--gold-dark));
    font-weight: 600;
    font-size: 15px;
    color: var(--ink-dark);
  }
  .product-description {
    position: absolute;
    left: 0;
    width: 100%;
    top: 806px;
    margin: 0;
    text-align: center;
    font-weight: 400;
    font-size: 14px;
    line-height: 19px;
    color: var(--soft-white);
  }
  .product-volume {
    position: absolute;
    left: 0;
    width: 100%;
    top: 910px;
    text-align: center;
    font-weight: 500;
    font-size: 17px;
    letter-spacing: 0.5px;
    color: var(--ink-dark);
  }
</style>
</head>
<body>
<main class="canvas">
  <section class="label">
    <div class="brand-band">
      <span class="brand-name">Velvet Grove</span>
    </div>
    <div class="ingredient-art" role="img" aria-label="Illustration of avocado halves, leaves, a honey dipper and a drop of honey"></div>
    <h1 class="product-title">AVOCADO &amp;<br>HONEY</h1>
    <div class="product-type">shampoo</div>
    <div class="product-benefit">MOISTURE REPAIR</div>
    <div class="infusion-ribbon">Infused W/biotin + Rosemary</div>
    <p class="product-description">Gently Cleanses and Hydrates<br>For Retention, Moisture And Softness</p>
    <div class="product-volume">300 ML / 10 FL OZ</div>
  </section>
</main>
</body>
</html>
```